Investment Company Business Card Design

We need a Business Card design for a new company based in Boston called "Velm Investment". We are cooperating with local real estate and construction companies. Our company is very actively and aggressively acquiring primarily residential investment properties either to buy and hold long term or for purposes or renovating and repositioning for re-sale in the market. In addition, we undertake some development projects and acquisitions as opportunities present themselves. the final design should contains information about “Velm" the river boat. we are tenacious, indomitable, and the business have a favorable wind throughout the voyage for all our investment.
sample Info. on Design:
Tusa Merrick
CEO
555-xxx-xxxx
418 Harlow St. Suite 507, Corvale, ME 04187
Please provide a template also, that we can edit the info later.
Reason: i just got new LOGO Design attached will be use in Business Card Design.
Construction

```html
<!DOCTYPE html>
<html lang="en">
<head>
<meta charset="utf-8">
<title>Velm Investment – Business Card</title>
<link href="https://fonts.googleapis.com/css2?family=Cinzel:wght@500&family=EB+Garamond:wght@400&display=swap" rel="stylesheet">
<style>
  :root {
    --backdrop: #2b2622;
    --card-black: #0b0b0b;
    --card-charcoal: #1a1a1a;
    --card-white: #f3f3f3;
    --gold: #c9a664;
    --gold-deep: #a9874a;
    --silver: #9b9b9b;
    --ink: #151515;
  }
  * { box-sizing: border-box; margin: 0; padding: 0; }
  html, body {
    width: 1200px; height: 800px; overflow: hidden;
    background: var(--backdrop);
  }
  .stage {
    position: relative; width: 1200px; height: 800px;
    display: flex; align-items: center; justify-content: center; gap: 50px;
  }
  .card {
    position: relative; width: 525px; height: 300px; overflow: hidden;
    box-shadow: 0 10px 30px rgba(0,0,0,.45);
  }

  /* Front */
  .card--front { background: var(--card-black); }
  .edge-band {
    position: absolute; top: 0; width: 18px; height: 100%;
    display: flex; flex-direction: column;
  }
  .edge-band--left { left: 0; }
  .edge-band--right { right: 0; }
  .edge-band span { flex: 1; }
  .edge-band .gold { background: var(--gold); }
  .edge-band .silver { background: var(--silver); }

  .wordmark {
    position: absolute; inset: 0;
    display: flex; align-items: center; justify-content: center; gap: 14px;
  }
  .wordmark__dot {
    width: 16px; height: 16px; border-radius: 50%;
    background: var(--gold);
  }
  .wordmark__name {
    font-family: "Cinzel", serif; font-weight: 500;
    font-size: 34px; letter-spacing: 2px; color: var(--gold);
  }

  /* Back */
  .card--back { display: flex; }
  .back__brand {
    width: 45%; background: var(--card-white);
    display: flex; align-items: center; justify-content: center; gap: 9px;
  }
  .back__brand .wordmark__dot { width: 11px; height: 11px; background: var(--ink); }
  .back__brand .wordmark__name { font-size: 19px; letter-spacing: 1px; color: var(--ink); }

  .back__details {
    width: 55%; position: relative;
    background: linear-gradient(160deg, var(--card-black) 0%, var(--card-black) 45%, var(--card-charcoal) 100%);
    padding: 40px 26px 0 34px;
  }
  .person__name {
    font-family: "Cinzel", serif; font-weight: 500;
    font-size: 22px; letter-spacing: 1.5px; color: var(--gold);
  }
  .person__title {
    font-family: "EB Garamond", serif; font-size: 13px;
    color: var(--gold-deep); margin-top: 4px; margin-left: 12px; letter-spacing: 1px;
  }
  .contact {
    position: absolute; left: 34px; right: 20px; bottom: 48px; list-style: none;
    font-family: "EB Garamond", serif; font-size: 15px; color: var(--gold);
  }
  .contact li { display: flex; gap: 10px; align-items: flex-start; margin-top: 6px; line-height: 1.3; }
  .contact svg { width: 13px; height: 13px; margin-top: 3px; flex: none; fill: var(--gold); }
</style>
</head>
<body>
<main class="stage">

  <section class="card card--front" aria-label="Card front">
    <div class="edge-band edge-band--left"><span class="gold"></span><span class="silver"></span></div>
    <div class="wordmark">
      <span class="wordmark__dot"></span>
      <span class="wordmark__name">Velm Investment</span>
    </div>
    <div class="edge-band edge-band--right"><span class="silver"></span><span class="gold"></span></div>
  </section>

  <section class="card card--back" aria-label="Card back">
    <div class="back__brand">
      <span class="wordmark__dot"></span>
      <span class="wordmark__name">Velm Investment</span>
    </div>
    <div class="back__details">
      <h1 class="person__name">TUSA MERRICK</h1>
      <p class="person__title">CEO</p>
      <ul class="contact">
        <li>
          <svg viewBox="0 0 16 16" aria-hidden="true"><path d="M3 1h3l1.5 4-2 1.3a9 9 0 0 0 4.2 4.2l1.3-2 4 1.5v3a2 2 0 0 1-2 2A13 13 0 0 1 1 3a2 2 0 0 1 2-2z"/></svg>
          <span>555-xxx-xxxx</span>
        </li>
        <li>
          <svg viewBox="0 0 16 16" aria-hidden="true"><path d="M8 1 0 8h2v7h4v-5h4v5h4V8h2z"/></svg>
          <span>418 Harlow St. Suite 507, Corvale<br>ME 04187</span>
        </li>
      </ul>
    </div>
  </section>

</main>
</body>
</html>
```